Chocolate covered bananas

“I am starting a new venture making chocolate coated frozen bananas. At start up I intend to have 4 different types:
3 will be single bananas ( Dark Chocolate, Dark chocolate with sprinkles and Dark Chocolate & Almonds) sold in individual packets, 70MM(W) x 215mm(L)

The other will be Banana Pops (smaller pieces of banana) sold in a 500g bag and then packed in a 165mm(L) x 50mm(W) X 165mm(H) cardboard box

The packaging will need my logo the wording “Chocolate Coated Frozen Banana” and the slogan “Sweet Bite Delight” on it. A picture of a Banana and Chocolate (The chocolate can be on the banana, getting poured on it, or even beside it).
I would like the words “Zero Trans-fat” on both the packaging (3 variations) and the 500g container along with “Healthy Dessert Treat” on the Container.

I need the Ingredients and nutritional information on the back"

one version can be submitted within the Contest period, however the winner is required to provide all 4 versions as part of the project.

Good Luck
Updates

JUST A QUICK NOTE THE BANANAS WILL BE ON A ICE-CREAM STICK AND THE BANANA POPS WILL BE ON A POPSICLE STICK.

Here are a couple of examples from places in America (no competition to me I am in another country) I'm am looking for something similar in size. as the packets in wholly mangoes and the cartons in gretas melons. http://www.wholly-mangoes.net/products.php and http://www.gretasmelons.com/our-products/ I hope this helps Regards Colin.

Hi I am getting some great designs Most are dark brown (or chocolate ) in colour they look good however most ice cream packs are dark and I think in order for these to stand out they need to be brighter with the chocolate as a secondary colour. Regards Colin.

Hi all great designs it will be very hard to pick. just a quick note I made a spelling mistake in my brief it is HEALTHY DESSERT TREAT (NOT DESERT) SORRY Regards Colin.

I would like to thank everyone for there time and effort they have put in to my packaging design contest. I am meeting with the packaging company on Thursday and will have a decision Thursday night. Regards Colin.

Target Market(s)

I plan to go down the track that these are a healthy tasty fun treat.
I will be using real Bananas and Real chocolate.

```html
<!DOCTYPE html>
<html lang="en">
<head>
<meta charset="utf-8">
<title>Purely Plantains Packaging Project</title>
<link rel="stylesheet" href="https://fonts.googleapis.com/css2?family=Tinos:wght@400&family=Oswald:wght@600;700&family=Arimo:wght@400&display=swap">
<style>
  :root {
    --sky: #3fb4d8;
    --sky-light: #9fe0f2;
    --sky-deep: #1f93bd;
    --choc: #3b2013;
    --banana: #f2e200;
    --cream: #ffffff;
    --red: #d7161d;
    --orange: #f08a00;
    --green: #17892f;
    --badge: #8cc63f;
    --ink: #111111;
    --serif: "Tinos", "Times New Roman", serif;
    --condensed: "Oswald", "Arial Narrow", sans-serif;
    --sans: "Arimo", Arial, sans-serif;
  }
  * { box-sizing: border-box; margin: 0; padding: 0; }
  html, body { width: 1017px; height: 1200px; overflow: hidden; background: #fff; }
  .board { position: relative; width: 1017px; height: 1200px; font-family: var(--sans); color: var(--ink); }

  .project-title { position: absolute; left: 578px; top: 30px; font-family: var(--condensed); font-weight: 700; font-size: 22px; letter-spacing: .2px; }

  .flavour-legend { position: absolute; left: 588px; top: 104px; font-family: var(--condensed); font-weight: 700; font-size: 22px; line-height: 26px; }
  .flavour-legend p { margin-bottom: 18px; color: var(--red); }
  .flavour-legend .sprinkles { color: var(--orange); }
  .flavour-legend .almonds { color: var(--green); }
  .legend-brace { position: absolute; left: 730px; top: 112px; }
  .legend-note { position: absolute; left: 775px; top: 178px; font-size: 15px; }

  .nutrition-brace { position: absolute; left: 92px; top: 336px; }
  .nutrition-note { position: absolute; left: 104px; top: 382px; font-size: 15px; }
  .logo-brace { position: absolute; left: 300px; top: 1074px; }
  .logo-note { position: absolute; left: 328px; top: 1106px; font-size: 15px; }

  /* shared pack surface */
  .pack { position: absolute; overflow: hidden;
    background: radial-gradient(circle at 50% 85%, var(--sky-light) 0%, var(--sky) 45%, var(--sky-deep) 100%); }
  .pack .drips { position: absolute; left: 0; top: 0; width: 100%; height: 62%; }
  .pack .brand { position: absolute; display: flex; align-items: center; justify-content: center; border-radius: 50%; background: var(--choc); border: 2px solid var(--banana); color: var(--banana); font-family: var(--serif); text-align: center; line-height: 1; }
  .pack .name-line { position: absolute; font-family: var(--serif); white-space: nowrap; line-height: 1; }
  .pack .white { color: var(--cream); }
  .pack .yellow { color: var(--banana); }
  .pack .trans-fat { position: absolute; border-radius: 50%; background: var(--badge); border: 2px solid var(--banana); color: #fff; display: flex; flex-direction: column; align-items: center; justify-content: center; font-family: var(--condensed); font-weight: 700; line-height: 1; }
  .pack .flavour { position: absolute; font-family: var(--condensed); font-weight: 700; color: var(--red); line-height: 1; white-space: nowrap; }
  .pack .count { position: absolute; font-family: var(--condensed); font-weight: 700; text-align: center; line-height: .9; color: #fff; }
  .pack .count b { color: var(--red); display: block; }
  .pack .weight { position: absolute; color: #fff; font-family: var(--condensed); font-weight: 600; }

  /* six pack box front */
  .box-front { left: 27px; top: 20px; width: 513px; height: 305px; }
  .box-front .brand { left: 14px; top: 14px; width: 76px; height: 76px; font-size: 12px; }
  .banana-photo { position: absolute; left: 140px; top: 130px; width: 350px; height: 125px; border-radius: 50% 50% 45% 45% / 30% 30% 70% 70%;
    background: linear-gradient(180deg, #f8e96a, #f0cf1c 60%, #c9a40e); }
  .nutrition-table { position: absolute; left: 62px; top: 273px; display: flex; gap: 3px; }
  .nutrition-table div { width: 19px; height: 32px; border: 1px solid #fff; border-radius: 4px; font-size: 6px; color: #fff; text-align: center; padding-top: 3px; }
  .nutrition-table span { display: block; margin-top: 7px; background: #fff; color: var(--ink); font-size: 6px; padding: 1px 0; }

  /* single wrappers */
  .wrapper { height: 130px; border-left: 12px solid var(--flavour); border-right: 12px solid var(--flavour); }
  .wrapper .brand { left: 8px; top: 8px; width: 34px; height: 34px; font-size: 6px; border-width: 1px; }
  .wrapper .name-line { font-size: 21px; }
  .wrapper .trans-fat { width: 26px; height: 26px; font-size: 9px; border-width: 1px; }
  .wrapper .flavour { font-size: 13px; }
  .wrapper .sub { font-family: var(--condensed); font-weight: 700; font-size: 10px; position: absolute; line-height: 1; color: var(--flavour); }
  .wrapper .count { font-size: 11px; }
  .wrapper .count b { font-size: 12px; }
  .wrapper .weight { font-size: 6px; }
  .wrapper-dark { --flavour: var(--red); left: 370px; top: 835px; width: 262px; }
  .wrapper-almonds { --flavour: var(--green); left: 675px; top: 785px; width: 287px; }
  .wrapper-sprinkles { --flavour: var(--orange); left: 473px; top: 982px; width: 290px; }

  .pop-photo { position: absolute; left: 60px; top: 868px; width: 310px; height: 200px;
    background: radial-gradient(ellipse at 40% 45%, #3a2c2c 0%, #231a1a 45%, rgba(255,255,255,0) 72%); }

  .brand-mark { position: absolute; left: 810px; top: 1006px; width: 150px; height: 150px; border-radius: 50%; background: var(--choc); border: 5px solid var(--banana); display: flex; align-items: center; justify-content: center; text-align: center; font-family: var(--serif); font-size: 24px; line-height: 1.1; color: var(--banana); }
</style>
</head>
<body>
<svg width="0" height="0" style="position:absolute" aria-hidden="true">
  <defs>
    <symbol id="chocolate-drips" viewBox="0 0 100 100" preserveAspectRatio="none">
      <path fill="#3b2013" d="M0,0 H100 V38 C98,38 97,40 97,55 C97,68 91,68 91,55 C91,40 89,36 86,36 C83,36 82,40 82,62 C82,76 76,76 76,62 C76,42 74,38 70,38 C67,38 66,42 66,50 C66,60 61,60 61,50 C61,40 59,36 56,36 C53,36 52,42 52,70 C52,84 46,84 46,70 C46,42 44,38 40,38 C37,38 36,42 36,54 C36,66 31,66 31,54 C31,40 29,36 26,36 C23,36 22,42 22,64 C22,76 16,76 16,64 C16,42 14,38 10,38 C7,38 6,42 6,52 C6,62 1,62 1,52 C1,44 0,40 0,40 Z"/>
    </symbol>
  </defs>
</svg>

<main class="board">
  <h1 class="project-title">PURELY PLANTAINS PACKAGING PROJECT</h1>

  <div class="flavour-legend">
    <p>DARK CHOCOLATE</p>
    <p>DARK CHOCOLATE<br><span class="sprinkles">&amp; SPRINKLES</span></p>
    <p>DARK CHOCOLATE<br><span class="almonds">&amp; ALMONDS</span></p>
  </div>
  <svg class="legend-brace" width="40" height="160" viewBox="0 0 40 160"><path d="M4 4 Q18 4 18 20 V64 Q18 80 34 80 Q18 80 18 96 V140 Q18 156 4 156" fill="none" stroke="#111" stroke-width="6"/></svg>
  <p class="legend-note">3 colours for 3 tastes</p>

  <section class="pack box-front">
    <svg class="drips"><use href="#chocolate-drips"/></svg>
    <div class="brand">Purely Plantains</div>
    <span class="name-line white" style="left:133px;top:34px;font-size:44px">Chocolate</span>
    <span class="name-line white" style="left:300px;top:56px;font-size:44px">Coated</span>
    <span class="name-line yellow" style="left:133px;top:78px;font-size:44px">Frozen</span>
    <span class="name-line yellow" style="left:290px;top:88px;font-size:44px">Banana</span>
    <div class="banana-photo" role="img" aria-label="Photograph of a ripe yellow banana"></div>
    <div class="trans-fat" style="left:441px;top:128px;width:56px;height:56px;font-size:20px">0%<small style="font-size:8px">TRANS-FAT</small></div>
    <span class="flavour" style="left:28px;top:208px;font-size:24px">DARK CHOCOLATE</span>
    <div class="count" style="left:466px;top:210px;font-size:20px"><b style="font-size:34px">6</b>pack</div>
    <span class="weight" style="left:20px;top:282px;font-size:14px">500g</span>
    <div class="nutrition-table">
      <div>Cal<span>5%</span></div>
      <div>Fat<span>0%</span></div>
      <div>Sat<span>2gr</span></div>
      <div>Sug<span>2gr</span></div>
      <div>Salt<span>2gr</span></div>
      <div>Pro<span>2gr</span></div>
    </div>
  </section>
  <svg class="nutrition-brace" width="130" height="40" viewBox="0 0 130 40"><path d="M4 4 Q4 18 20 18 H50 Q65 18 65 34 Q65 18 80 18 H110 Q126 18 126 4" fill="none" stroke="#111" stroke-width="6"/></svg>
  <p class="nutrition-note">nutrition facts</p>

  <section class="pack wrapper wrapper-dark">
    <svg class="drips"><use href="#chocolate-drips"/></svg>
    <div class="brand">Purely Plantains</div>
    <span class="name-line white" style="left:74px;top:34px">Chocolate</span>
    <span class="name-line white" style="left:154px;top:46px">Coated</span>
    <span class="name-line yellow" style="left:74px;top:56px">Frozen</span>
    <span class="name-line yellow" style="left:138px;top:60px">Banana</span>
    <div class="trans-fat" style="left:216px;top:22px">0%</div>
    <span class="weight" style="left:74px;top:82px">100g</span>
    <span class="flavour" style="left:90px;top:79px">DARK CHOCOLATE</span>
    <div class="count" style="left:210px;top:62px"><b>1</b>pack</div>
  </section>

  <section class="pack wrapper wrapper-almonds">
    <svg class="drips"><use href="#chocolate-drips"/></svg>
    <div class="brand">Purely Plantains</div>
    <span class="name-line white" style="left:75px;top:34px">Chocolate</span>
    <span class="name-line white" style="left:157px;top:46px">Coated</span>
    <span class="name-line yellow" style="left:85px;top:56px">Frozen</span>
    <span class="name-line yellow" style="left:150px;top:60px">Banana</span>
    <div class="trans-fat" style="left:238px;top:22px">0%</div>
    <span class="weight" style="left:88px;top:82px">100g</span>
    <span class="flavour" style="left:103px;top:79px">DARK CHOCOLATE</span>
    <span class="sub" style="left:118px;top:93px">&amp; ALMONDS</span>
    <div class="count" style="left:232px;top:62px"><b>1</b>pack</div>
  </section>

  <section class="pack wrapper wrapper-sprinkles">
    <svg class="drips"><use href="#chocolate-drips"/></svg>
    <div class="brand">Purely Plantains</div>
    <span class="name-line white" style="left:78px;top:34px">Chocolate</span>
    <span class="name-line white" style="left:160px;top:46px">Coated</span>
    <span class="name-line yellow" style="left:90px;top:56px">Frozen</span>
    <span class="name-line yellow" style="left:154px;top:60px">Banana</span>
    <div class="trans-fat" style="left:240px;top:22px">0%</div>
    <span class="weight" style="left:90px;top:82px">100g</span>
    <span class="flavour" style="left:104px;top:79px">DARK CHOCOLATE</span>
    <span class="sub" style="left:114px;top:93px">&amp; SPRINKLES</span>
    <div class="count" style="left:234px;top:62px"><b>1</b>pack</div>
  </section>

  <div class="pop-photo" role="img" aria-label="Photograph of a chocolate coated frozen banana on a wooden stick with the brand name printed on the stick"></div>
  <svg class="logo-brace" width="90" height="34" viewBox="0 0 90 34"><path d="M4 4 Q4 16 18 16 H32 Q45 16 45 30 Q45 16 58 16 H72 Q86 16 86 4" fill="none" stroke="#111" stroke-width="6"/></svg>
  <p class="logo-note">logo</p>

  <div class="brand-mark">Purely<br>Plantains</div>
</main>
</body>
</html>
```